Income Tax and Accounting Brochure

I need a brochure using my new logo (file attached). I do tax work and accounting work. I am an EA (QDX Enrolled Agent - logo attached) and would like this incorporated into the brochure. I also have a MSA in Accounting. Please incorporate the text that I have provided in the brochure.

Target Market(s)

Tax Clients - both business and individuals

Industry/Entity Type

Accounting

Colors
0054AA
0677BA
7BADD7
CADEEF
E8F1F8

Requirements
Must have
• Use my logo and the QDX EA file in the brochure
Nice to have
• I would like to see a brochure that I can customize with my own text if possible.

```html
<!DOCTYPE html>
<html lang="en">
<head>
<meta charset="utf-8">
<title>Harbor Ledger – Tax Planning Brochure</title>
<link href="https://fonts.googleapis.com/css2?family=Source+Sans+3:ital,wght@0,400;0,600;0,700;1,400;1,700&display=swap" rel="stylesheet">
<style>
:root{
  --navy:#0054AA;
  --blue:#0677BA;
  --sky:#7BADD7;
  --mist:#CADEEF;
  --ice:#E8F1F8;
  --red:#C8161D;
  --red-deep:#8E0E14;
  --ink:#3a3a3a;
  --bg:#d6d7d9;
  --white:#ffffff;
}
*{margin:0;padding:0;box-sizing:border-box}
html,body{width:764px;height:1200px;overflow:hidden;background:var(--bg)}
body{font-family:"Source Sans 3",Arial,sans-serif;color:var(--ink);position:relative}
.spread{position:absolute;left:55px;width:672px;height:522px;box-shadow:0 8px 10px -6px rgba(0,0,0,.35)}
.spread--outside{top:57px}
.spread--inside{top:639px}
.panel{position:absolute;top:0;height:522px;overflow:hidden}
.panel--left{left:0;width:219px}
.panel--mid{left:219px;width:220px}
.panel--right{left:439px;width:233px}
.abs{position:absolute}
.fill{position:absolute;inset:0}
.red-panel{background:linear-gradient(160deg,#d21a22 0%,var(--red) 45%,var(--red-deep) 100%);color:var(--white)}
.blue-panel{background:linear-gradient(180deg,var(--blue) 0%,var(--navy) 100%);color:var(--white)}
.web-pill{position:absolute;left:50%;transform:translateX(-50%);height:17px;padding:0 9px;border-radius:9px;font-size:7.6px;font-weight:600;display:flex;align-items:center;gap:3px;white-space:nowrap}
.web-pill--red{background:var(--red);color:var(--white)}
.web-pill--white{background:var(--white);color:var(--navy)}
.web-pill i{display:inline-block;width:6px;height:6px;border-radius:50%;border:1px solid currentColor}
.footer-bar{position:absolute;left:0;right:0;height:13px;background:var(--white);color:var(--navy);font-size:7.2px;font-weight:600;display:flex;align-items:center;justify-content:center;gap:3px}
.footer-bar i{display:inline-block;width:6px;height:6px;border-radius:50%;border:1px solid currentColor}
.body-copy{font-size:9.2px;line-height:12.3px;text-align:justify}
.body-copy p+p{margin-top:8px}
/* outside left */
.about-photo{left:0;top:0;width:219px;height:230px}
.portrait{left:116px;top:138px;width:95px;height:95px;border-radius:50%;border:3px solid var(--navy);background:radial-gradient(circle at 50% 40%,#d8b79a,#9b6e4f 70%,#5a3b2a)}
.ea-badge{left:14px;top:221px;width:36px;height:22px;border:2px solid var(--sky);background:var(--ice)}
.about-title{left:13px;top:260px;font-size:12.4px;font-weight:700;color:var(--navy);line-height:14px}
.about-sub{left:13px;top:274px;font-size:9px;color:var(--navy)}
.about-copy{left:13px;top:293px;width:195px}
.tagline{left:0;width:219px;top:479px;text-align:center;font-size:9px;font-weight:700;font-style:italic;color:var(--navy)}
/* outside mid */
.tax-photo{left:43px;top:53px;width:134px;height:134px;border-radius:50%;border:5px solid var(--white);background:radial-gradient(circle at 55% 45%,#d9b46a,#8a6a3a 60%,#3e3326)}
.intro{left:30px;width:160px;top:203px;font-size:8.3px;line-height:10.1px;text-align:center}
.cta-title{left:0;width:220px;top:309px;text-align:center;font-size:15.5px;font-weight:700;line-height:22px;letter-spacing:.2px}
.contact-label{left:0;width:220px;top:368px;text-align:center;font-size:11px;font-weight:700;line-height:14px}
.contact-lines{left:0;width:220px;top:393px;text-align:center;font-size:8.3px;line-height:11.1px;font-style:normal}
/* outside right */
.brand{left:0;width:233px;top:26px;display:flex;align-items:center;justify-content:center;gap:7px}
.brand-dot{width:28px;height:28px;border-radius:50%;background:var(--navy)}
.brand-name{font-size:12.5px;font-weight:700;color:var(--navy);line-height:13px}
.cover-title{left:0;width:233px;top:446px;text-align:center;font-size:26px;font-weight:700;color:var(--white);line-height:30px}
.cover-sub{left:0;width:233px;top:477px;text-align:center;font-size:12.4px;color:var(--white);line-height:14px}
/* inside */
.why-title{left:13px;top:46px;font-size:16.5px;line-height:21px;font-weight:600}
.why-copy{left:13px;top:99px;width:194px}
.team-photo{left:0;top:0;width:219px;height:522px}
.gets-title{left:0;width:220px;top:42px;text-align:center;font-size:12.2px;font-weight:700}
.benefit{position:absolute;left:10px;width:198px;display:flex;gap:11px;align-items:flex-start}
.benefit-icon{flex:0 0 32px;width:32px;height:32px;margin-top:2px}
.benefit p{font-size:7.5px;line-height:9.4px;text-align:justify}
.cta-small{left:0;width:220px;top:371px;text-align:center;font-size:11.2px;font-weight:700;line-height:16px}
.phone-pill{left:40px;top:416px;width:140px;height:18px;border-radius:9px;background:var(--white);color:var(--navy);font-size:10.4px;font-weight:700;display:flex;align-items:center;justify-content:center;gap:5px}
.closing{left:20px;width:180px;top:453px;text-align:center;font-size:8.3px;line-height:10.2px}
.books-photo{left:0;top:0;width:233px;height:522px}
.books-title{left:21px;top:249px;font-size:16px;line-height:21.5px;font-weight:600}
.books-copy{left:21px;top:301px;width:198px}
.books-copy p+p{margin-top:9px}
.seminar-note{left:21px;top:452px;width:198px;font-size:7.6px;line-height:9.6px;font-style:italic;text-align:justify}
</style>
</head>
<body>

<!-- OUTSIDE SPREAD -->
<section class="spread spread--outside">

  <article class="panel panel--left" style="background:var(--white)">
    <svg class="abs about-photo" viewBox="0 0 219 230" role="img" aria-label="Photo of colleagues reviewing charts on a tablet at a desk">
      <defs><linearGradient id="deskTone" x1="0" y1="0" x2="1" y2="1"><stop offset="0" stop-color="#9aa7b6"/><stop offset=".6" stop-color="#dfe5ec"/><stop offset="1" stop-color="#f4f6f9"/></linearGradient></defs>
      <path d="M0 0H219V150C170 170 110 210 0 222Z" fill="url(#deskTone)"/>
      <path d="M219 140C175 165 120 205 20 225L0 230C110 222 170 190 219 170Z" fill="var(--navy)"/>
      <path d="M219 170C170 195 110 222 0 230H219Z" fill="var(--white)"/>
    </svg>
    <div class="abs portrait" role="img" aria-label="Portrait photo of the principal"></div>
    <div class="abs ea-badge"></div>
    <h2 class="abs about-title">ABOUT MARIAN T HOLLOWAY,</h2>
    <div class="abs about-sub">MSA EA (Principal)</div>
    <div class="abs about-copy body-copy">
      <p>I have a Masters' Degree in accounting and am an QDX Enrolled Agent. I am also a LedgerPro Advanced Certified Consultant in both the online and desktop products including Enterprise and Point of Sale. I provide individual and small business tax services, Accounting, bookkeeping, QDX representation, insurance audit representation, business license assistance and more.</p>
      <p style="text-align:left">I have experience working with a wide variety of clients from the point where they first decide they want to start a business. They are often unsure about what to do first- I have a lot of experience to offer you.</p>
    </div>
    <div class="abs tagline">What a joy it is to watch success in action!</div>
    <div class="web-pill web-pill--red" style="top:499px"><i></i>www.harborledger.example</div>
  </article>

  <article class="panel panel--mid red-panel">
    <div class="abs tax-photo" role="img" aria-label="Photo of stacked coins, a pocket watch and letter blocks spelling tax"></div>
    <p class="abs intro">If you are looking for a blend of personal service and expertise, you have come to the right place! We offer a broad range of services for business owners, executives and independent professionals.<br><br>Our rates are affordable.<br>We are experienced and friendly.</p>
    <h2 class="abs cta-title">CONTACT US FOR &nbsp;A<br>FREE CONSULTATION</h2>
    <h3 class="abs contact-label">CONTACT US</h3>
    <address class="abs contact-lines">
      Harbor Ledger Accounting &amp; Consulting, LLC<br>
      4820 Quarry Mill Rd, PO Box 18<br>
      Linden Falls, VA 20455<br>
      Phone: (555)014-2270<br>
      Fax: (555)019-3381<br>
      info@harborledger.example
    </address>
    <div class="web-pill web-pill--white" style="top:499px"><i></i>www.harborledger.example</div>
  </article>

  <article class="panel panel--right" style="background:var(--white)">
    <div class="brand"><span class="brand-dot"></span><span class="brand-name">HARBOR LEDGER<br>CONSULTING, LLC</span></div>
    <svg class="fill" viewBox="0 0 233 522" role="img" aria-label="Photo of a team meeting in a bright glass-walled conference room">
      <defs>
        <linearGradient id="roomTone" x1="0" y1="0" x2="0" y2="1"><stop offset="0" stop-color="#c9d3dc"/><stop offset=".5" stop-color="#e6eaee"/><stop offset="1" stop-color="#8f9aa6"/></linearGradient>
        <linearGradient id="coverBlue" x1="0" y1="0" x2="0" y2="1"><stop offset="0" stop-color="var(--blue)"/><stop offset="1" stop-color="var(--navy)"/></linearGradient>
      </defs>
      <rect x="0" y="66" width="233" height="360" fill="url(#roomTone)"/>
      <path d="M0 330C40 380 55 430 70 522H0Z" fill="var(--red)"/>
      <path d="M0 390C60 390 110 330 160 280C190 250 215 240 233 236V522H0Z" fill="url(#coverBlue)"/>
      <path d="M0 395C70 390 120 330 165 285C195 255 218 246 233 243" fill="none" stroke="var(--sky)" stroke-width="2" opacity=".7"/>
    </svg>
    <h1 class="abs cover-title">TAX PLANNING</h1>
    <div class="abs cover-sub">Income Tax &amp; Accounting</div>
    <div class="web-pill web-pill--red" style="top:499px"><i></i>www.harborledger.example</div>
  </article>
</section>

<!-- INSIDE SPREAD -->
<section class="spread spread--inside">

  <article class="panel panel--left blue-panel">
    <svg class="abs team-photo" viewBox="0 0 219 522" role="img" aria-label="Photo of two smiling women reviewing paperwork together">
      <defs><linearGradient id="teamTone" x1="0" y1="0" x2="1" y2="1"><stop offset="0" stop-color="#cfd6dd"/><stop offset=".5" stop-color="#a59684"/><stop offset="1" stop-color="#4c4b52"/></linearGradient></defs>
      <path d="M0 395C70 392 150 360 219 330V522H0Z" fill="url(#teamTone)"/>
      <path d="M0 388C70 385 150 353 219 322V336C150 368 70 398 0 402Z" fill="var(--sky)"/>
    </svg>
    <h2 class="abs why-title">Tax Preparation<br>&nbsp;WHY HIRE US?</h2>
    <div class="abs why-copy body-copy">
      <p>Preparing your own income tax return can be a task that leaves you with more questions than answers. According to a study released by the US Government's Federal Review Bureau last year, most taxpayers (77% of 71 million taxpayers) believe they benefited from using a professional tax preparer.</p>
      <p>Whether we like it or not, today's tax laws are so complicated that filing a relatively simple return can be confusing.</p>
      <p>It is just too easy to overlook deductions and credits to which you are entitled. Even if you use a computer software program there's no substitute for the assistance of an experienced tax professional.</p>
    </div>
  </article>

  <article class="panel panel--mid red-panel">
    <h2 class="abs gets-title">HERE'S WHAT YOUR GET...</h2>

    <div class="benefit" style="top:83px">
      <svg class="benefit-icon" viewBox="0 0 32 32"><circle cx="16" cy="16" r="15" fill="none" stroke="#fff" stroke-width="1.4"/><rect x="8" y="9" width="16" height="11" rx="1" fill="none" stroke="#fff" stroke-width="1.3"/><path d="M13 23h6M16 20v3" stroke="#fff" stroke-width="1.3"/><circle cx="16" cy="14.5" r="3" fill="none" stroke="#fff" stroke-width="1.1"/></svg>
      <p>Your tax return will be checked and rechecked by our computer software identifying potential problems the QDX may look at more closely and reviewing the math to limit QDX contacts.</p>
    </div>
    <div class="benefit" style="top:161px">
      <svg class="benefit-icon" viewBox="0 0 32 32"><circle cx="16" cy="16" r="15" fill="none" stroke="#fff" stroke-width="1.4"/><rect x="8" y="12" width="16" height="10" rx="1" fill="none" stroke="#fff" stroke-width="1.3"/><circle cx="16" cy="17" r="2.6" fill="none" stroke="#fff" stroke-width="1.1"/><path d="M11 9l10-2" stroke="#fff" stroke-width="1.3"/></svg>
      <p>Your tax return can be filed electronically so you will get a refund back quicker.</p>
    </div>
    <div class="benefit" style="top:211px">
      <svg class="benefit-icon" viewBox="0 0 32 32"><circle cx="16" cy="16" r="15" fill="none" stroke="#fff" stroke-width="1.4"/><circle cx="13" cy="14" r="4.5" fill="none" stroke="#fff" stroke-width="1.3"/><circle cx="20" cy="20" r="3.5" fill="none" stroke="#fff" stroke-width="1.3"/><circle cx="13" cy="14" r="1.3" fill="#fff"/></svg>
      <p>Our staff will show you how to adjust your payroll withholding to get more money back each week. Why give the QDX an interest free loan for up to 16 months.</p>
    </div>
    <div class="benefit" style="top:281px">
      <svg class="benefit-icon" viewBox="0 0 32 32"><circle cx="16" cy="16" r="15" fill="none" stroke="#fff" stroke-width="1.4"/><path d="M9 23v-4M13 23v-6M17 23v-8M21 23v-10" stroke="#fff" stroke-width="1.8"/><path d="M9 15l5-4 4 2 5-5" fill="none" stroke="#fff" stroke-width="1.2"/></svg>
      <p>We will show you potential deductions to limit your tax liability for next year. In addition, we will give you a sheet of commonly overlooked deductions to limit the following year's tax liability.</p>
    </div>

    <h2 class="abs cta-small">CONTACT US FOR &nbsp;A<br>FREE CONSULTATION</h2>
    <div class="abs phone-pill">
      <svg width="10" height="10" viewBox="0 0 10 10"><circle cx="5" cy="5" r="4.4" fill="none" stroke="currentColor" stroke-width=".9"/><path d="M3.2 2.8c.3 1.9 1.6 3.4 3.6 4l.6-.9-1.1-.6-.5.5c-.8-.4-1.3-1-1.6-1.8l.5-.5-.6-1.1z" fill="currentColor"/></svg>
      (555)014-2270
    </div>
    <p class="abs closing">We go beyond tax compliance and proactively recommend tax saving strategies to maximize your after-tax income.</p>
    <div class="footer-bar" style="top:505px"><i></i>www.harborledger.example</div>
  </article>

  <article class="panel panel--right blue-panel">
    <svg class="abs books-photo" viewBox="0 0 233 522" role="img" aria-label="Photo of a young woman working on a laptop in a cafe">
      <defs><linearGradient id="cafeTone" x1="0" y1="0" x2="1" y2="1"><stop offset="0" stop-color="#e9ece9"/><stop offset=".5" stop-color="#b8a48c"/><stop offset="1" stop-color="#6a5647"/></linearGradient></defs>
      <path d="M0 0H233V240C200 190 160 150 90 140C50 135 20 125 0 115Z" fill="url(#cafeTone)"/>
      <path d="M0 115C20 125 50 135 90 140C160 150 200 190 233 240V250C200 200 160 160 90 150C50 145 20 135 0 125Z" fill="var(--sky)"/>
    </svg>
    <h2 class="abs books-title">Books a Mess:<br>NO PROBLEM!</h2>
    <div class="abs books-copy body-copy">
      <p>If you own a small business and haven't kept up your bookkeeping, don't worry. We can help you.</p>
      <p>We'll prepare your bookkeeping for the year, prepare a full Schedule C, as well as your personal income tax return.</p>
      <p>Then we'll help you set up an easy system that allows you to keep your books in tip-top shape next year.</p>
    </div>
    <p class="abs seminar-note">We make it a priority to enhance our mastery of the current tax law, complex tax code, and new tax regulations by attending frequent tax seminars.</p>
    <div class="footer-bar" style="top:505px"><i></i>www.harborledger.example</div>
  </article>
</section>

</body>
</html>
```